Halvard Atelier Business cards

Design our business cards and eventually a logo. The company is based in Paris, its activity is the retailing via internet of luxury home furniture (like Vambrelli, Bercusa, tarvoni...) Our clients are international andwith a high sense of aesthetics. The design shall communicate wealth and trust with a high quality and aesthetic sense, pure lines Company Name is Halvard AtelierExplanation of the name: usually people who wants to buy furniture usually go in a showroom. Today they go in showroom to test the furniture and they search for the price on internet, which is a "Halvard atelier".We will not be a e-commerce site. Our site will be (another project) a presentation site which purpose is to reach qualified prospects. Then everything will be handled by phone, meeting etc.The business card must be professional as we will negotiate with many luxury brands, opportunity to represent them on our site, prices etc.As far as the color are concerned mostly black and whithe or grey. The font of the Halvard Atelier name shall have some impact.

Target Market(s)

High-end furniture and buyers of luxury goods, international customers, mostly women who handle such projects.
We also deal with professional buyers (hotels as an example) and luxury brands

Contact Information for Business Card

standard format 85x55, lanscape card, square corners will be printed on thick high quality paper (300 or 350g)

Font styles to use
Sans Serif

Colors

Designer to choose colors to be used in the design.

Requirements
Must have
• Must be white, as the paper will be high quality, the paper will enhance the card.
• Name of the brand Halvard atelier (with specific font which make it very nice looking and catch the attention. similar to Calibri or Calibri
• Name of person (will give you the name later (4 names and position)
• the position of the person
• Mobile phone, e-mail, Physical address 27, rue Fenouillard, 75005 Paris, France (courrier only) our web site www.halvardatelier.fr
• The card must be simple and class
Nice to have
• Font of the address is smaller than the rest,
• Calibri font or similar on recto side with the name of the company which may look similar to the picture inserted in the brief.
• The grey color in the picture inserted is ok for us
Should not have
• Any parallel lines which represent the name of the company
• Any heavy design If you go on internet sites which present the furniture all designs are pure lines and high quality craftsmanship. To have an idea of our targetted client or brand we will be in touch: https://www.casavelumi.it/projects/
• Note that the picture added below is what we use, now as mail signature, up to you to have a better design etc.

```html
<!DOCTYPE html>
<html lang="en">
<head>
<meta charset="utf-8">
<title>Halvard Atelier — Business Card</title>
<link rel="stylesheet" href="https://fonts.googleapis.com/css2?family=Saira+Condensed:wght@400;500&display=swap">
<style>
  :root {
    --card-white: #ffffff;
    --gold: #b8862a;
    --text-dark: #2a2a2a;
    --rule-grey: #9a9a9a;
    --backdrop: #e4e4e4;
  }
  * { margin: 0; padding: 0; box-sizing: border-box; }
  html, body {
    width: 1200px;
    height: 1171px;
    overflow: hidden;
    background: var(--backdrop);
    font-family: "Saira Condensed", "Arial Narrow", sans-serif;
  }
  .canvas {
    position: relative;
    width: 1200px;
    height: 1171px;
  }
  .card {
    position: absolute;
    left: 0;
    top: 0;
    width: 1200px;
    height: 697px;
    background: var(--card-white);
    overflow: hidden;
  }
  .brand {
    position: absolute;
    top: 108px;
    left: 0;
    width: 1200px;
    text-align: center;
    color: var(--gold);
    font-size: 60px;
    font-weight: 400;
    letter-spacing: 0.42em;
    text-indent: 0.42em;
    line-height: 1;
    text-transform: uppercase;
  }
  .person {
    position: absolute;
    right: 722px;
    top: 306px;
    text-align: right;
    color: var(--gold);
  }
  .person__name {
    font-size: 64px;
    line-height: 1;
    font-weight: 400;
    letter-spacing: 0.02em;
  }
  .person__role {
    margin-top: 8px;
    font-size: 44px;
    line-height: 1;
    letter-spacing: 0.03em;
  }
  .divider {
    position: absolute;
    left: 523px;
    top: 328px;
    width: 2px;
    height: 153px;
    background: var(--rule-grey);
  }
  .contact {
    position: absolute;
    left: 570px;
    top: 320px;
    list-style: none;
    color: var(--text-dark);
    font-size: 40px;
    line-height: 58px;
    letter-spacing: 0.03em;
  }
  .address {
    position: absolute;
    top: 602px;
    left: 0;
    width: 1200px;
    text-align: center;
    color: var(--text-dark);
    font-size: 30px;
    line-height: 1;
    letter-spacing: 0.02em;
  }
</style>
</head>
<body>
<main class="canvas">
  <section class="card">
    <h1 class="brand">Halvard Atelier</h1>
    <div class="person">
      <p class="person__name">Elodie Marchand</p>
      <p class="person__role">Assistant</p>
    </div>
    <div class="divider"></div>
    <ul class="contact">
      <li>+33 1 48 27 61 90</li>
      <li>elodie.marchand@velmail.com</li>
      <li>www.halvardatelier.fr</li>
    </ul>
    <p class="address">27, rue Fenouillard, 75005 Paris, France</p>
  </section>
</main>
</body>
</html>
```